Simple Business Card Design for Foodie

Job:

Make a very simple, minimalist business card design with my details including adjusted logo. One side to be white (with logo & text). Other side to be yellow - try plain or with logo (or part of logo eg Z). Need business card to have continuity with website.

Logo:
Our logo is made from a free download font website:
http://www.typegrotto.net/search.php?q=rubber
but the spacing/kerning needs correcting/adjusting as the font spaces unevenly between letters (see attached files). Need logo to be very crisp/sharp when printed.

Printing:
We will be using Kelvo.com so the design needs to conform to their requirements, see here:

http://uk.kelvo.com/products/velour/business-cards.html (scroll down for dimensions and guidelines)

Design:

must say "plant-based food consulting" underneath logo or somewhere
no address needed in contact section
sharp corners (not rounded)
one side white, one side yellow

name: Harriet Colwick
1xmobile number: +44 7700900461
1xtwiiter: @pelkoadvice
website address www.marrowlanekitchen.com
email address pelko@marrowlanekitchen.com

Should be easy quick job, prompt + detailed feedback given, am online in UK 9am-10pm for next 3 days. Website is www.marrowlanekitchen.com

Industry/Entity Type

Business

Requirements
Must have
• The logo must be corrected. The kerning is not right.

Please use a warm-grey for text

Please submit in matt format, we will be printing matt finish.

Should not have
• Avoid using banners or curvy highlights

Please avoid using black

Please avoid submitting in gloss finish

```html
<!DOCTYPE html>
<html lang="en">
<head>
<meta charset="utf-8">
<title>Pelko business card</title>
<link rel="stylesheet" href="https://fonts.googleapis.com/css2?family=Julius+Sans+One&display=swap">
<style>
  :root {
    --page: #e6e4e0;
    --card-white: #ffffff;
    --card-yellow: #f7ec4a;
    --warm-grey: #6b645c;
    --warm-grey-soft: #8c857c;
    --rule: #b9b2a8;
  }
  * { margin: 0; padding: 0; box-sizing: border-box; }
  html, body {
    width: 1200px; height: 927px; overflow: hidden;
    background: var(--page);
    font-family: "Julius Sans One", sans-serif;
    color: var(--warm-grey);
  }
  .sheet {
    width: 1200px; height: 927px;
    display: flex; align-items: center; justify-content: center; gap: 40px;
  }
  .card {
    position: relative; width: 540px; height: 309px;
    border-radius: 0;
    box-shadow: 0 2px 10px rgba(60, 55, 50, .12);
  }
  .card-front { background: var(--card-white); }
  .card-back {
    background: var(--card-yellow);
    display: flex; flex-direction: column; align-items: center; justify-content: center;
  }
  .wordmark {
    color: var(--warm-grey);
    font-size: 56px; letter-spacing: 8px; line-height: 1;
  }
  .tagline {
    font-size: 12px; letter-spacing: 2px; color: var(--warm-grey-soft);
    margin-top: 12px;
  }
  .card-front .brand {
    position: absolute; left: 0; right: 0; top: 44px; text-align: center;
  }
  .identity {
    position: absolute; left: 30px; top: 200px; width: 210px;
    text-align: center;
  }
  .identity .name { font-size: 16px; letter-spacing: 1px; }
  .identity .role { font-size: 11px; margin-top: 6px; color: var(--warm-grey-soft); }
  .divider {
    position: absolute; left: 254px; top: 186px; width: 1px; height: 92px;
    background: var(--rule);
  }
  .contacts {
    position: absolute; left: 270px; top: 188px; list-style: none;
    font-size: 11px;
  }
  .contacts li { display: flex; align-items: center; gap: 8px; height: 22px; }
  .contacts svg { width: 12px; height: 12px; flex: none; }
</style>
</head>
<body>
<main class="sheet">
  <section class="card card-front" aria-label="Card front">
    <div class="brand">
      <div class="wordmark">PELKO</div>
      <p class="tagline">plant-based food consulting</p>
    </div>
    <div class="identity">
      <p class="name">Harriet Colwick</p>
      <p class="role">Founder</p>
    </div>
    <div class="divider"></div>
    <ul class="contacts">
      <li><svg viewBox="0 0 12 12" aria-hidden="true"><circle cx="6" cy="6" r="6" fill="var(--warm-grey)"/><rect x="4.2" y="2.8" width="3.6" height="6.4" rx=".6" fill="var(--card-white)"/></svg>+44 7700900461</li>
      <li><svg viewBox="0 0 12 12" aria-hidden="true"><circle cx="6" cy="6" r="6" fill="var(--warm-grey)"/></svg>@pelkoadvice</li>
      <li><svg viewBox="0 0 12 12" aria-hidden="true"><circle cx="6" cy="6" r="6" fill="var(--warm-grey)"/><circle cx="6" cy="6" r="3" fill="none" stroke="var(--card-white)" stroke-width=".8"/><path d="M3 6 H9 M6 3 V9" stroke="var(--card-white)" stroke-width=".7"/></svg>www.marrowlanekitchen.com</li>
      <li><svg viewBox="0 0 12 12" aria-hidden="true"><circle cx="6" cy="6" r="6" fill="var(--warm-grey)"/><rect x="3" y="4" width="6" height="4" fill="var(--card-white)"/><path d="M3 4 L6 6.3 L9 4" stroke="var(--warm-grey)" stroke-width=".7" fill="none"/></svg>pelko@marrowlanekitchen.com</li>
    </ul>
  </section>

  <section class="card card-back" aria-label="Card back">
    <div class="wordmark">PELKO</div>
    <p class="tagline">plant-based food consulting</p>
  </section>
</main>
</body>
</html>
```